Organic CBD topicals needs product labels for body butters, roll on oils and massage oil candles

We are looking for product labels that fit our growing brand, We are yogi's making organic CBD infused topicals that help people with pain relief and healing through plant based creams and oils, naturally, without side effects. We have body butter balms that come in 2oz tins, we have massage oil candles in 6oz, mandala design tins with a lid, we have infused essential oils in frosted glass bottles with healing gemstone roller balls, we also make lip balms in both 1/2 oz tins and lip balm sticks, as well as a 2oz twist up body butter balm. I would like the labels to have a yogi/chakra feel to them. The body butter balms come in different strengths, so it would be great if the strongest 600mg start at the base chakra, using the chakre color scale and go up from there. 300mg, 150mg then pure CBD, then up the chakra scale for the other products, 1:1, 3:1 and 30:1 for the roll on essential oils and massage oil candles.

You can see our products here: www.lunavalebotanics.org

Kivo Body Butter Balm label 2 1/2" round.
Matching 2" label for the bottom of the tin with ingredients & instructions.
Massage Oil Candle label 1 1/2 round
Bottom of Candle label 2" round for ingredients & instructions
Spiraled Kivo Body Butter Label 4 1'2 wide x 2 1/2 tall Square
Twist up lip balm label can be 2 1/4 w x 1 1/2 tall
Lip Balm tin label 1" round

Target Market(s)

Everyone that has pain, injuries, headaches, skin conditions, etc... and wants to deal with them naturally, without big pharma and their terrible medicines that come with killer side effects.

Font styles to use
Serif
Sans Serif

Requirements
Must have
• A yogi look and feel, chakra colors, symbols and our logo featured prominently
Should not have
• a corporate look or feel

```html
<!DOCTYPE html>
<html lang="en">
<head>
<meta charset="utf-8">
<title>Lunavale Kivo Body Butter Balm – Chakra Labels</title>
<link rel="stylesheet" href="https://fonts.googleapis.com/css2?family=Cinzel:wght@400;500&family=Raleway:wght@300;400;500&display=swap">
<style>
  :root {
    --canvas: #f3f3f1;
    --label-white: #ffffff;
    --label-shade: #f1f1ef;
    --rim-gold: #c9b96a;
    --rim-steel: #b9bcbf;
    --ink: #2a2a2a;
    --ink-soft: #555555;
    --lavender: #5a2f86;
    --lemon-ink: #3b2a10;
    --badge: #1f1f1f;
    --heart: #5fa843;
    --root: #f0504c;
    --throat: #4a7cbd;
  }
  * { margin: 0; padding: 0; box-sizing: border-box; }
  html, body {
    width: 735px;
    height: 1200px;
    overflow: hidden;
    background: var(--canvas);
  }
  .label-sheet {
    width: 735px;
    height: 1200px;
    display: flex;
    flex-direction: column;
  }
  .chakra-variant {
    height: 400px;
    display: flex;
    flex-direction: column;
    align-items: center;
    justify-content: center;
    gap: 14px;
  }
  .chakra-variant--heart  { --chakra: var(--heart); }
  .chakra-variant--root   { --chakra: var(--root); }
  .chakra-variant--throat { --chakra: var(--throat); }

  .tin-label { width: 340px; height: 340px; display: block; }
  .tin-label .rim { fill: var(--rim-steel); }
  .tin-label .field { fill: var(--label-white); }
  .tin-label .gold-band { fill: none; stroke: var(--rim-gold); stroke-width: 7; }
  .tin-label .gold-line { fill: none; stroke: var(--rim-gold); stroke-width: 1; }
  .tin-label .swirl { fill: var(--chakra); }
  .tin-label .brand-mark { fill: none; stroke: var(--ink-soft); stroke-width: 1.6; }
  .tin-label .brand-name {
    font-family: "Cinzel", serif; font-size: 19px; fill: var(--ink); letter-spacing: 0.5px;
  }
  .tin-label .brand-tagline {
    font-family: "Cinzel", serif; font-size: 7px; fill: var(--ink); letter-spacing: 0.3px;
  }
  .tin-label .product-name {
    font-family: "Raleway", sans-serif; font-weight: 500; font-size: 21px; fill: #ffffff;
  }
  .tin-label .product-line {
    font-family: "Raleway", sans-serif; font-weight: 400; font-size: 16px; fill: #ffffff;
  }
  .tin-label .product-line--light { font-weight: 300; opacity: 0.85; }
  .tin-label .rule { stroke: #ffffff; stroke-width: 1; opacity: 0.8; }
  .tin-label .product-type {
    font-family: "Raleway", sans-serif; font-weight: 500; font-size: 13px; fill: var(--ink); letter-spacing: 1px;
  }
  .tin-label .scent-primary {
    font-family: "Raleway", sans-serif; font-size: 12px; fill: var(--lavender);
  }
  .tin-label .scent-secondary {
    font-family: "Raleway", sans-serif; font-size: 12px; fill: var(--lemon-ink);
  }
  .tin-label .scent-arc { stroke: #ffffff; stroke-width: 1.5; fill: none; opacity: 0.9; }
  .tin-label .certification-badge { fill: var(--badge); }
  .tin-label .certification-ring { fill: none; stroke: #ffffff; stroke-width: 0.8; opacity: 0.6; }

  .chakra-caption {
    font-family: "Raleway", sans-serif;
    font-size: 15px;
    font-weight: 400;
    color: var(--chakra);
    letter-spacing: 0.3px;
  }
</style>
</head>
<body>
<main class="label-sheet">

  <section class="chakra-variant chakra-variant--heart">
    <svg class="tin-label" viewBox="0 0 340 340" aria-label="Kivo Body Butter Balm label, heart chakra green">
      <circle class="rim" cx="170" cy="170" r="169"/>
      <circle class="field" cx="170" cy="170" r="158"/>
      <circle class="gold-band" cx="170" cy="170" r="150"/>
      <circle class="gold-line" cx="170" cy="170" r="145"/>
      <path class="swirl" d="M200 29 A62 62 0 0 1 175 142 A92 92 0 0 0 170 315 A145 145 0 0 0 200 29 Z"/>
      <circle class="brand-mark" cx="140" cy="82" r="26"/>
      <text class="brand-name" x="140" y="134" text-anchor="middle">LUNAVALE</text>
      <text class="brand-tagline" x="140" y="146" text-anchor="middle">ORGANIC BOTANICALS</text>
      <text class="product-name" x="186" y="188" text-anchor="middle">KIVO</text>
      <text class="product-line" x="186" y="208" text-anchor="middle">ORGANIC</text>
      <text class="product-line product-line--light" x="186" y="227" text-anchor="middle">BODY BUTTER</text>
      <line class="rule" x1="134" y1="233" x2="238" y2="233"/>
      <text class="product-type" x="186" y="249" text-anchor="middle">‖ BALM ‖</text>
      <text class="scent-primary" x="190" y="272" text-anchor="middle" transform="rotate(8 190 272)">LAVENDER</text>
      <text class="scent-secondary" x="190" y="289" text-anchor="middle" transform="rotate(-6 190 289)">&amp; LEMON</text>
      <path class="scent-arc" d="M150 298 Q190 306 228 294"/>
      <circle class="certification-badge" cx="276" cy="196" r="17"/>
      <circle class="certification-ring" cx="276" cy="196" r="12"/>
    </svg>
    <p class="chakra-caption">HEART CHAKRA (GREEN COLOR)</p>
  </section>

  <section class="chakra-variant chakra-variant--root">
    <svg class="tin-label" viewBox="0 0 340 340" aria-label="Kivo Body Butter Balm label, root chakra red">
      <circle class="rim" cx="170" cy="170" r="169"/>
      <circle class="field" cx="170" cy="170" r="158"/>
      <circle class="gold-band" cx="170" cy="170" r="150"/>
      <circle class="gold-line" cx="170" cy="170" r="145"/>
      <path class="swirl" d="M200 29 A62 62 0 0 1 175 142 A92 92 0 0 0 170 315 A145 145 0 0 0 200 29 Z"/>
      <circle class="brand-mark" cx="140" cy="82" r="26"/>
      <text class="brand-name" x="140" y="134" text-anchor="middle">LUNAVALE</text>
      <text class="brand-tagline" x="140" y="146" text-anchor="middle">ORGANIC BOTANICALS</text>
      <text class="product-name" x="186" y="188" text-anchor="middle">KIVO</text>
      <text class="product-line" x="186" y="208" text-anchor="middle">ORGANIC</text>
      <text class="product-line product-line--light" x="186" y="227" text-anchor="middle">BODY BUTTER</text>
      <line class="rule" x1="134" y1="233" x2="238" y2="233"/>
      <text class="product-type" x="186" y="249" text-anchor="middle">‖ BALM ‖</text>
      <text class="scent-primary" x="190" y="272" text-anchor="middle" transform="rotate(8 190 272)">LAVENDER</text>
      <text class="scent-secondary" x="190" y="289" text-anchor="middle" transform="rotate(-6 190 289)">&amp; LEMON</text>
      <path class="scent-arc" d="M150 298 Q190 306 228 294"/>
      <circle class="certification-badge" cx="276" cy="196" r="17"/>
      <circle class="certification-ring" cx="276" cy="196" r="12"/>
    </svg>
    <p class="chakra-caption">ROOT CHAKRA (RED COLOR)</p>
  </section>

  <section class="chakra-variant chakra-variant--throat">
    <svg class="tin-label" viewBox="0 0 340 340" aria-label="Kivo Body Butter Balm label, throat chakra blue">
      <circle class="rim" cx="170" cy="170" r="169"/>
      <circle class="field" cx="170" cy="170" r="158"/>
      <circle class="gold-band" cx="170" cy="170" r="150"/>
      <circle class="gold-line" cx="170" cy="170" r="145"/>
      <path class="swirl" d="M200 29 A62 62 0 0 1 175 142 A92 92 0 0 0 170 315 A145 145 0 0 0 200 29 Z"/>
      <circle class="brand-mark" cx="140" cy="82" r="26"/>
      <text class="brand-name" x="140" y="134" text-anchor="middle">LUNAVALE</text>
      <text class="brand-tagline" x="140" y="146" text-anchor="middle">ORGANIC BOTANICALS</text>
      <text class="product-name" x="186" y="188" text-anchor="middle">KIVO</text>
      <text class="product-line" x="186" y="208" text-anchor="middle">ORGANIC</text>
      <text class="product-line product-line--light" x="186" y="227" text-anchor="middle">BODY BUTTER</text>
      <line class="rule" x1="134" y1="233" x2="238" y2="233"/>
      <text class="product-type" x="186" y="249" text-anchor="middle">‖ BALM ‖</text>
      <text class="scent-primary" x="190" y="272" text-anchor="middle" transform="rotate(8 190 272)">LAVENDER</text>
      <text class="scent-secondary" x="190" y="289" text-anchor="middle" transform="rotate(-6 190 289)">&amp; LEMON</text>
      <path class="scent-arc" d="M150 298 Q190 306 228 294"/>
      <circle class="certification-badge" cx="276" cy="196" r="17"/>
      <circle class="certification-ring" cx="276" cy="196" r="12"/>
    </svg>
    <p class="chakra-caption">THROAT CHAKRA (BLUE COLOR)</p>
  </section>

</main>
</body>
</html>
```